New florist business website design

Number 1 want is an easy to navigate & check out website
Needs to be beautiful and eye catching as well.
This is an online only business (no shop front)
Rustic and blush pinks, neutrals, woods, leaves
Customers need to be able to go onto my website, select something they want to buy but have the option to use a drop down box to change colours of the flowers, or add notes to make changes to the arrangement

Industry/Entity Type

Florist

Coding

Coded - Design and coding required

Number of Pages Required

5+ page

Colors
f9d9e8
fff2ec
fffefc

Requirements
Must have
• Drop down menu to take you to other pages for Arrangements, bouquets, everlasting arrangements, gifts, contact
Be able to purchase and “add to basket”
Checkout page
Nice to have
• Be able to add my own photos once I’ve taken new ones
Should not have
• Tacky images or clip art

```html
<!DOCTYPE html>
<html lang="en">
<head>
<meta charset="utf-8">
<title>Briar &amp; Bloom — Florist</title>
<link rel="stylesheet" href="https://fonts.googleapis.com/css2?family=Rubik:wght@300;400;500;700&family=Roboto:wght@400;500;700&display=swap">
<style>
:root{
  --blush:#f9d9e8;
  --blush-soft:#fbe9ef;
  --cream:#fff2ec;
  --ivory:#fffefc;
  --paper:#fdf7f3;
  --peach:#fbe3cc;
  --card:#fde8e3;
  --ink:#1f1f1f;
  --text:#333;
  --rose:#f29ac6;
  --line:#e8e0dc;
}
*{box-sizing:border-box;margin:0;padding:0}
html,body{width:1200px;height:4488px;overflow:hidden}
body{position:relative;background:var(--paper);font-family:Roboto,Arial,sans-serif;color:var(--text)}
.abs{position:absolute}
.pill{position:absolute;display:flex;align-items:center;justify-content:center;border-radius:30px;font-family:Rubik,Arial,sans-serif;font-weight:500;text-transform:uppercase;font-size:15px;letter-spacing:.3px}
.pill.dark{background:var(--ink);color:#fff}
.pill.light{background:#fff;color:var(--ink)}

/* header */
.topbar{position:absolute;left:0;top:0;width:1200px;height:101px;background:var(--blush-soft)}
.brand-badge{position:absolute;left:148px;top:-10px;width:150px;height:150px;border-radius:50%;background:#fff;display:flex;align-items:center;justify-content:center;z-index:3}
.brand-badge span{font-family:Rubik,sans-serif;font-weight:400;font-size:20px;color:var(--ink)}
.search{position:absolute;left:503px;top:31px;width:333px;height:44px;background:#fff;border:1px solid var(--line);border-radius:3px;font-size:12px;color:#666;padding:14px 14px}
.search svg{position:absolute;right:12px;top:15px}
.cart-label{position:absolute;left:965px;top:37px;font-size:12px;line-height:17px;color:var(--ink)}
.navbar{position:absolute;left:0;top:101px;width:1200px;height:49px;background:#fff}
.navbar a{position:absolute;top:17px;font-family:Rubik,sans-serif;font-weight:500;font-size:13px;color:var(--ink);text-decoration:none;display:flex;align-items:center;gap:6px}

/* hero */
.hero{position:absolute;left:0;top:150px;width:1200px;height:611px;
  background:
    radial-gradient(ellipse 220px 200px at 470px 390px,rgba(238,92,52,.95),rgba(238,92,52,0) 100%),
    radial-gradient(ellipse 170px 220px at 770px 130px,rgba(246,214,190,.95),rgba(246,214,190,0) 100%),
    radial-gradient(ellipse 260px 320px at 660px 470px,rgba(120,70,40,.9),rgba(120,70,40,0) 100%),
    radial-gradient(ellipse 260px 500px at 760px 330px,rgba(245,243,238,.95),rgba(245,243,238,0) 100%),
    radial-gradient(ellipse 240px 300px at 1080px 300px,rgba(168,112,176,.7),rgba(168,112,176,0) 100%),
    linear-gradient(100deg,#5d4a30 0%,#7a6a40 20%,#6f8a52 38%,#c8a06a 55%,#e8dccf 72%,#5f7a48 100%)}
.hero-title{position:absolute;left:141px;top:188px;font-family:Rubik,sans-serif;color:#fff;font-size:57px;line-height:63px;font-weight:300}
.hero-title b{font-weight:700}
.dots{position:absolute;left:570px;top:528px;display:flex;gap:9px}
.dots i{width:13px;height:13px;border-radius:50%;background:#fff;display:block}

/* featured grid */
.section-title{position:absolute;left:0;width:1200px;text-align:center;font-family:Rubik,sans-serif;font-weight:500;font-size:38px;color:var(--ink)}
.card{position:absolute;width:216px;text-align:center}
.card .photo{height:214px;border-radius:8px 8px 0 0}
.card .price{margin-top:20px;font-size:17px;color:var(--ink)}
.card .desc{margin-top:6px;font-size:15px;line-height:23px;color:var(--ink)}
.card .btn{margin:12px auto 0;width:185px;height:42px;border:1.5px solid var(--ink);border-radius:22px;display:flex;align-items:center;justify-content:space-between;padding:0 16px 0 22px;font-family:Rubik,sans-serif;font-weight:500;font-size:14px;color:var(--ink)}

/* everlasting */
.everlasting{position:absolute;left:0;top:1779px;width:1200px;height:521px;
  background:
    radial-gradient(ellipse 150px 130px at 760px 410px,rgba(236,196,128,.95),rgba(236,196,128,0) 100%),
    radial-gradient(ellipse 110px 90px at 770px 90px,rgba(120,80,60,.9),rgba(120,80,60,0) 100%),
    radial-gradient(ellipse 140px 260px at 780px 300px,rgba(240,236,226,.95),rgba(240,236,226,0) 100%),
    radial-gradient(ellipse 160px 180px at 1090px 160px,rgba(150,130,60,.85),rgba(150,130,60,0) 100%),
    linear-gradient(90deg,#f1ece7 0%,#e6ddd3 40%,#9a8a74 62%,#6f5f4e 78%,#c8beb0 100%)}
.blob{position:absolute;background:var(--blush);border-radius:42% 48% 44% 50%/46% 42% 50% 44%}
.copy{position:absolute;text-align:center;font-size:15.5px;line-height:22.5px;color:var(--text)}

/* categories */
.tile{position:absolute;top:2305px;width:398px;height:278px}
.tile h3{position:absolute;font-family:Rubik,sans-serif;font-weight:500;font-size:18px;color:#fff}
.tile p{position:absolute;font-size:14px;line-height:21px;color:#fff}

/* newsletter */
.newsletter{position:absolute;left:0;top:3136px;width:1200px;height:540px;
  background:
    radial-gradient(ellipse 160px 200px at 200px 300px,rgba(96,84,170,.75),rgba(96,84,170,0) 100%),
    radial-gradient(ellipse 180px 90px at 600px 520px,rgba(240,120,170,.8),rgba(240,120,170,0) 100%),
    radial-gradient(ellipse 120px 100px at 1080px 150px,rgba(70,140,60,.8),rgba(70,140,60,0) 100%),
    radial-gradient(ellipse 130px 90px at 120px 460px,rgba(214,170,120,.85),rgba(214,170,120,0) 100%),
    radial-gradient(ellipse 140px 80px at 1060px 380px,rgba(240,200,40,.7),rgba(240,200,40,0) 100%),
    linear-gradient(180deg,#eef1f2,#e2e8ea 60%,#e9edee)}
.email{position:absolute;left:308px;top:3416px;width:403px;height:40px;border-radius:20px;background:#fff;border:1px solid #ddd;font-size:13px;color:#777;padding:12px 26px}

/* benefits */
.benefits{position:absolute;left:111px;top:3571px;width:960px;height:357px;background:var(--peach)}
.benefit{position:absolute}
.benefit .ico{position:absolute;left:0;top:0;width:76px;height:76px;border-radius:50%;background:var(--rose);border:5px solid #fff;display:flex;align-items:center;justify-content:center}
.benefit h4{position:absolute;left:95px;top:10px;font-family:Rubik,sans-serif;font-weight:500;font-size:15px;color:var(--ink);white-space:nowrap}
.benefit p{position:absolute;left:95px;top:32px;width:180px;font-size:13.5px;line-height:17.5px;color:var(--text)}
.vsep{position:absolute;top:3600px;width:1px;height:300px;background:#f3d0b4}

/* footer */
.footer{position:absolute;left:0;top:3993px;width:1200px;height:371px;background:var(--blush-soft)}
.footer h5{position:absolute;font-family:Rubik,sans-serif;font-weight:500;font-size:18px;color:var(--ink)}
.footer ul{position:absolute;list-style:none;font-size:13.5px;line-height:29px;color:var(--text)}
.contact-row{position:absolute;left:841px;font-size:13.5px;line-height:19px;color:var(--text)}
.contact-row svg{position:absolute;left:0;top:1px}
.contact-row span{display:block;margin-left:37px}
.bottombar{position:absolute;left:0;top:4364px;width:1200px;height:124px;background:#fff}
.social{position:absolute;top:4412px;width:32px;height:32px;border:2px solid var(--ink);border-radius:50%}
.paycard{position:absolute;top:4418px;width:40px;height:25px;border-radius:3px}
</style>
</head>
<body>

<header>
  <div class="topbar"></div>
  <div class="brand-badge"><span>Briar &amp; Bloom</span></div>
  <div class="search">Search products...
    <svg width="14" height="14" viewBox="0 0 14 14"><circle cx="6" cy="6" r="4.5" fill="none" stroke="#333" stroke-width="1.6"/><line x1="9.3" y1="9.3" x2="13" y2="13" stroke="#333" stroke-width="1.6"/></svg>
  </div>
  <svg class="abs" style="left:862px;top:38px" width="30" height="30" viewBox="0 0 30 30"><circle cx="15" cy="10" r="6" fill="none" stroke="#222" stroke-width="1.6"/><path d="M3 27c1-6 6-9 12-9s11 3 12 9z" fill="none" stroke="#222" stroke-width="1.6"/></svg>
  <svg class="abs" style="left:918px;top:32px" width="38" height="36" viewBox="0 0 38 36"><path d="M2 8h6l4 16h18l4-12H10" fill="none" stroke="#222" stroke-width="1.8"/><circle cx="14" cy="30" r="2.4" fill="#222"/><circle cx="27" cy="30" r="2.4" fill="#222"/><circle cx="32" cy="7" r="6" fill="#222"/><text x="32" y="10" font-size="8" fill="#fff" text-anchor="middle" font-family="Roboto,sans-serif">0</text></svg>
  <div class="cart-label">Shopping Cart<br>0 Items</div>
  <nav class="navbar">
    <a style="left:312px">HOME</a>
    <a style="left:392px">ARRANGEMENTS <svg width="8" height="5" viewBox="0 0 8 5"><path d="M1 1l3 3 3-3" fill="none" stroke="#222" stroke-width="1.2"/></svg></a>
    <a style="left:543px">BOUQUETS <svg width="8" height="5" viewBox="0 0 8 5"><path d="M1 1l3 3 3-3" fill="none" stroke="#222" stroke-width="1.2"/></svg></a>
    <a style="left:657px">EVERLASTING ARRANGEMENTS <svg width="8" height="5" viewBox="0 0 8 5"><path d="M1 1l3 3 3-3" fill="none" stroke="#222" stroke-width="1.2"/></svg></a>
    <a style="left:913px">GIFTS</a>
    <a style="left:991px">CONTACT</a>
  </nav>
</header>

<section class="hero" role="img" aria-label="Smiling florist holding a bouquet of orange tulips in a flower shop">
  <h1 class="hero-title">Briar &amp; Bloom<br><b>Best Selling</b><br>Flowers</h1>
  <div class="pill light" style="left:143px;top:400px;width:184px;height:46px">Add to basket</div>
  <div class="dots"><i></i><i></i><i></i></div>
</section>

<h2 class="section-title" style="top:808px">Featured Products</h2>

<section class="products">
  <div class="card" style="left:139px;top:939px"><div class="photo" role="img" aria-label="Mixed bouquet of white daisies, pink and purple blooms" style="background:radial-gradient(ellipse 95px 80px at 50% 42%,#e8467e 0%,#8a4cae 40%,#f4f0f2 62%,var(--card) 100%)"></div><div class="price">$38.00</div><div class="desc">Nemo enim ipsam voluptata<br>voluptas sit aspernatur</div><div class="btn">ADD TO CART <svg width="16" height="14" viewBox="0 0 16 14"><path d="M1 5h14l-2 8H3z" fill="#222"/><path d="M5 5l3-4 3 4" fill="none" stroke="#222" stroke-width="1.4"/></svg></div></div>
  <div class="card" style="left:375px;top:939px"><div class="photo" role="img" aria-label="Bouquet of deep red roses" style="background:radial-gradient(ellipse 90px 78px at 50% 40%,#d0142e 0%,#9a0c20 45%,#3f6a34 66%,var(--card) 100%)"></div><div class="price">$38.00</div><div class="desc">Nemo enim ipsam voluptata<br>voluptas sit aspernatur</div><div class="btn">ADD TO CART <svg width="16" height="14" viewBox="0 0 16 14"><path d="M1 5h14l-2 8H3z" fill="#222"/><path d="M5 5l3-4 3 4" fill="none" stroke="#222" stroke-width="1.4"/></svg></div></div>
  <div class="card" style="left:610px;top:939px"><div class="photo" role="img" aria-label="Bouquet of magenta and pink roses with greenery" style="background:radial-gradient(ellipse 95px 80px at 50% 42%,#e8368e 0%,#c24c9a 38%,#6f9a4a 62%,var(--card) 100%)"></div><div class="price">$38.00</div><div class="desc">Nemo enim ipsam voluptata<br>voluptas sit aspernatur</div><div class="btn">ADD TO CART <svg width="16" height="14" viewBox="0 0 16 14"><path d="M1 5h14l-2 8H3z" fill="#222"/><path d="M5 5l3-4 3 4" fill="none" stroke="#222" stroke-width="1.4"/></svg></div></div>
  <div class="card" style="left:843px;top:939px"><div class="photo" role="img" aria-label="Bouquet of pale green roses wrapped in brown paper" style="background:radial-gradient(ellipse 92px 80px at 50% 40%,#e6efc8 0%,#b4c47e 40%,#8a4a3a 62%,var(--card) 100%)"></div><div class="price">$38.00</div><div class="desc">Nemo enim ipsam voluptata<br>voluptas sit aspernatur</div><div class="btn">ADD TO CART <svg width="16" height="14" viewBox="0 0 16 14"><path d="M1 5h14l-2 8H3z" fill="#222"/><path d="M5 5l3-4 3 4" fill="none" stroke="#222" stroke-width="1.4"/></svg></div></div>

  <div class="card" style="left:139px;top:1340px"><div class="photo" role="img" aria-label="Soft peach and white rose bouquet" style="background:radial-gradient(ellipse 92px 80px at 50% 40%,#f7d0c2 0%,#e0a08c 40%,#e57a90 60%,var(--card) 100%)"></div><div class="price">$38.00</div><div class="desc">Nemo enim ipsam voluptata<br>voluptas sit aspernatur</div><div class="btn">ADD TO CART <svg width="16" height="14" viewBox="0 0 16 14"><path d="M1 5h14l-2 8H3z" fill="#222"/><path d="M5 5l3-4 3 4" fill="none" stroke="#222" stroke-width="1.4"/></svg></div></div>
  <div class="card" style="left:375px;top:1340px"><div class="photo" role="img" aria-label="White and lilac bridal bouquet" style="background:radial-gradient(ellipse 92px 80px at 50% 40%,#f6f2f6 0%,#cbb8d2 40%,#8a9a78 62%,var(--card) 100%)"></div><div class="price">$38.00</div><div class="desc">Nemo enim ipsam voluptata<br>voluptas sit aspernatur</div><div class="btn">ADD TO CART <svg width="16" height="14" viewBox="0 0 16 14"><path d="M1 5h14l-2 8H3z" fill="#222"/><path d="M5 5l3-4 3 4" fill="none" stroke="#222" stroke-width="1.4"/></svg></div></div>
  <div class="card" style="left:610px;top:1340px"><div class="photo" role="img" aria-label="Red rose bouquet tied with a red ribbon" style="background:radial-gradient(ellipse 85px 72px at 50% 36%,#dc1a2c 0%,#a60e1c 45%,#4a7038 64%,var(--card) 100%)"></div><div class="price">$38.00</div><div class="desc">Nemo enim ipsam voluptata<br>voluptas sit aspernatur</div><div class="btn">ADD TO CART <svg width="16" height="14" viewBox="0 0 16 14"><path d="M1 5h14l-2 8H3z" fill="#222"/><path d="M5 5l3-4 3 4" fill="none" stroke="#222" stroke-width="1.4"/></svg></div></div>
  <div class="card" style="left:843px;top:1340px"><div class="photo" role="img" aria-label="Pink and white rose bouquet with foliage" style="background:radial-gradient(ellipse 90px 80px at 50% 40%,#e0507e 0%,#f0e4e8 38%,#4f7a42 62%,var(--card) 100%)"></div><div class="price">$38.00</div><div class="desc">Nemo enim ipsam voluptata<br>voluptas sit aspernatur</div><div class="btn">ADD TO CART <svg width="16" height="14" viewBox="0 0 16 14"><path d="M1 5h14l-2 8H3z" fill="#222"/><path d="M5 5l3-4 3 4" fill="none" stroke="#222" stroke-width="1.4"/></svg></div></div>
</section>

<section class="everlasting" role="img" aria-label="Florist arranging a bouquet at a wooden workbench">
  <div class="blob" style="left:96px;top:41px;width:383px;height:375px"></div>
  <h2 class="abs" style="left:96px;top:92px;width:383px;text-align:center;font-family:Rubik,sans-serif;font-weight:500;color:var(--ink);font-size:38px;line-height:44px">Everlasting<br>Arrangements</h2>
  <p class="copy" style="left:130px;top:246px;width:315px">Sed ut perspiciatis unde omnis iste natus voluptatem accusantium doloremque laudantium, totam rem aperiam, eaque ipsa quae ab illo inventore</p>
  <div class="pill dark" style="left:211px;top:350px;width:160px;height:45px">Add to cart</div>
</section>

<section>
  <div class="tile" style="left:0;background:radial-gradient(ellipse 150px 170px at 60px 140px,#f4eee8 0%,#d87a9a 35%,#7a5a8a 60%,rgba(58,72,72,0) 100%),linear-gradient(90deg,#8a6a6a,#3e4a4a 55%,#33413f)" role="img" aria-label="White lilies and purple blooms on a slate background">
    <h3 style="left:218px;top:88px">BOUQUETS</h3>
    <p style="left:218px;top:116px">Lorem ipsum dolor sit<br>amet, consectetur</p>
    <div class="pill light" style="left:218px;top:169px;width:124px;height:30px;font-size:12px">Shop now</div>
  </div>
  <div class="tile" style="left:404px;background:radial-gradient(ellipse 80px 90px at 340px 80px,#e4a4b4,rgba(40,30,34,0) 100%),radial-gradient(ellipse 70px 70px at 60px 240px,#c4909e,rgba(40,30,34,0) 100%),linear-gradient(90deg,#2a2226,#161416 50%,#2e2428)" role="img" aria-label="Pink roses and peonies on a dark background">
    <h3 style="left:133px;top:88px">ARRANGEMENTS</h3>
    <p style="left:138px;top:116px;text-align:center">Lorem ipsum dolor sit<br>amet, consectetur</p>
    <div class="pill light" style="left:148px;top:172px;width:124px;height:30px;font-size:12px">Shop now</div>
  </div>
  <div class="tile" style="left:806px;width:394px;background:radial-gradient(ellipse 160px 150px at 300px 90px,#d0101e,rgba(90,8,16,0) 100%),radial-gradient(ellipse 110px 110px at 260px 250px,#b00c1a,rgba(90,8,16,0) 100%),linear-gradient(90deg,#2a1a1c,#4a1014 50%,#6a0a14)" role="img" aria-label="Close-up of red roses">
    <h3 style="left:35px;top:94px">GIFTS</h3>
    <p style="left:35px;top:122px">Lorem ipsum dolor sit<br>amet, consectetur</p>
    <div class="pill light" style="left:35px;top:180px;width:124px;height:30px;font-size:12px">Shop now</div>
  </div>
</section>

<section>
  <div class="blob" role="img" aria-label="Bouquet of pink tulips wrapped in kraft paper" style="left:105px;top:2665px;width:304px;height:401px;border-radius:8%;background:radial-gradient(ellipse 120px 80px at 50% 22%,#e83a64 0%,#f4a0b4 45%,rgba(249,217,232,0) 100%),radial-gradient(ellipse 70px 120px at 50% 68%,#7a5a4a 0%,#a08070 50%,rgba(249,217,232,0) 100%),var(--blush)"></div>
  <div class="blob" role="img" aria-label="Large bouquet of red roses with long green stems" style="left:793px;top:2665px;width:304px;height:401px;border-radius:8%;background:radial-gradient(ellipse 125px 95px at 50% 28%,#d0142e 0%,#a00e20 50%,rgba(249,217,232,0) 100%),radial-gradient(ellipse 45px 110px at 50% 78%,#3f6a30 0%,#5a8a44 50%,rgba(249,217,232,0) 100%),var(--blush)"></div>
  <h2 class="section-title" style="top:2703px">Featured Products</h2>
  <p class="copy" style="left:445px;top:2835px;width:310px">Sed ut perspiciatis unde omnis iste natus voluptatem accusantium doloremque laudantium, totam rem aperiam, eaque ipsa quae ab illo inventore</p>
  <div class="pill dark" style="left:523px;top:2947px;width:156px;height:42px">Add to cart</div>
</section>

<section class="newsletter" role="img" aria-label="Florist workbench with twine, ribbon, scissors, leaves and flowers">
  <h2 class="section-title" style="top:116px">Join our Newsletter</h2>
  <p class="abs" style="left:0;top:171px;width:1200px;text-align:center;font-size:13.5px;color:var(--ink)">Subscribe to our mailing list to receive updates</p>
</section>
<div class="email">Enter your E - mail</div>
<div class="pill dark" style="left:723px;top:3414px;width:155px;height:44px;font-size:14px">Subscribe</div>

<section class="benefits"></section>
<div class="vsep" style="left:431px"></div>
<div class="vsep" style="left:760px"></div>
<div class="benefit" style="left:136px;top:3602px"><div class="ico"><svg width="34" height="24" viewBox="0 0 34 24"><rect x="1" y="3" width="20" height="14" fill="#fff"/><path d="M21 7h7l5 5v5H21z" fill="#fff"/><circle cx="8" cy="20" r="3" fill="#fff"/><circle cx="26" cy="20" r="3" fill="#fff"/></svg></div><h4>FREE SHIPPING</h4><p>Lorem Ipsum is simply dummy text of the printing and types etting industry</p></div>
<div class="benefit" style="left:463px;top:3602px"><div class="ico"><svg width="30" height="30" viewBox="0 0 30 30"><rect x="4" y="6" width="22" height="20" rx="2" fill="none" stroke="#fff" stroke-width="2"/><line x1="4" y1="12" x2="26" y2="12" stroke="#fff" stroke-width="2"/><path d="M15 15v5h4" fill="none" stroke="#fff" stroke-width="2"/></svg></div><h4>30 DAYS RETURN</h4><p>Lorem Ipsum is simply dummy text of the printing and types etting industry</p></div>
<div class="benefit" style="left:782px;top:3602px"><div class="ico"><svg width="30" height="30" viewBox="0 0 30 30"><path d="M4 13h5v14H4zM11 27V13l6-10c3 0 3 3 2 6h7c2 0 3 2 2 4l-3 12c-1 2-2 2-3 2z" fill="#fff"/></svg></div><h4>SATIISFACTION</h4><p>Lorem Ipsum is simply dummy text of the printing and types etting industry</p></div>
<div class="benefit" style="left:136px;top:3782px"><div class="ico"><svg width="32" height="30" viewBox="0 0 32 30"><path d="M5 17a11 11 0 0 1 22 0" fill="none" stroke="#fff" stroke-width="2.5"/><rect x="3" y="16" width="6" height="9" rx="2" fill="#fff"/><rect x="23" y="16" width="6" height="9" rx="2" fill="#fff"/></svg></div><h4>SUPPORT</h4><p>Lorem Ipsum is simply dummy text of the printing and types etting industry</p></div>
<div class="benefit" style="left:463px;top:3782px"><div class="ico"><svg width="30" height="30" viewBox="0 0 30 30"><rect x="5" y="11" width="20" height="16" fill="none" stroke="#fff" stroke-width="2"/><rect x="3" y="7" width="24" height="5" fill="#fff"/><line x1="15" y1="7" x2="15" y2="27" stroke="#fff" stroke-width="2"/></svg></div><h4>FREE GIFT CARD</h4><p>Lorem Ipsum is simply dummy text of the printing and types etting industry</p></div>
<div class="benefit" style="left:782px;top:3782px"><div class="ico"><svg width="30" height="32" viewBox="0 0 30 32"><path d="M15 2l11 4v9c0 8-5 13-11 15C9 28 4 23 4 15V6z" fill="none" stroke="#fff" stroke-width="2"/><path d="M10 16l4 4 7-8" fill="none" stroke="#fff" stroke-width="2.5"/></svg></div><h4>SECURE PAYMENT</h4><p>Lorem Ipsum is simply dummy text of the printing and types etting industry</p></div>

<footer class="footer">
  <div class="abs" style="left:148px;top:120px;width:244px;text-align:center;font-family:Rubik,sans-serif;font-size:30px;font-weight:400;color:var(--ink)">Briar &amp; Bloom</div>
  <h5 style="left:430px;top:70px">MY ACCOUNT</h5>
  <ul style="left:430px;top:114px"><li>My Orders</li><li>My Bills</li><li>My Addresses</li><li>My Personal Information</li><li>My Vouchers</li><li>Site Map</li><li>Blog</li></ul>
  <h5 style="left:638px;top:70px">QUICK LINKS</h5>
  <ul style="left:638px;top:114px"><li>Home</li><li>About Us/Our Partner</li><li>Shop</li><li>Blog</li><li>Contact &amp; FAQ</li><li>Press and Awards</li></ul>
  <h5 style="left:841px;top:70px">CONTACT US</h5>
  <div class="contact-row" style="top:127px"><svg width="18" height="22" viewBox="0 0 18 22"><path d="M9 1a7 7 0 0 0-7 7c0 5 7 13 7 13s7-8 7-13a7 7 0 0 0-7-7z" fill="var(--rose)"/><circle cx="9" cy="8" r="2.5" fill="#fff"/></svg><span>Briar &amp; Bloom<br>75-137 enim ipsam<br>voluptatem quia</span></div>
  <div class="contact-row" style="top:199px"><svg width="20" height="20" viewBox="0 0 20 20"><path d="M4 1l4 4-2 3c1 3 3 5 6 6l3-2 4 4-3 3C8 19 1 12 1 4z" fill="var(--rose)"/></svg><span>Phone: 808 5550 0142</span></div>
  <div class="contact-row" style="top:231px"><svg width="20" height="15" viewBox="0 0 20 15"><rect x="0" y="0" width="20" height="15" rx="2" fill="var(--rose)"/><path d="M1 2l9 7 9-7" fill="none" stroke="#fff" stroke-width="1.5"/></svg><span>Email: info@briarbloom.com</span></div>
  <div class="contact-row" style="top:263px"><svg width="18" height="18" viewBox="0 0 18 18"><circle cx="9" cy="9" r="9" fill="var(--rose)"/><path d="M9 4v5h4" fill="none" stroke="#fff" stroke-width="1.6"/></svg><span>Open time: 8AM to 5PM.</span></div>
</footer>

<div class="bottombar"></div>
<p class="abs" style="left:145px;top:4420px;font-size:13.5px;color:var(--ink)">© 2021 Briar &amp; Bloom. All Rights Reserved.</p>
<span class="social" style="left:533px"></span>
<span class="social" style="left:582px"></span>
<span class="social" style="left:630px"></span>
<span class="social" style="left:679px"></span>
<span class="social" style="left:727px"></span>
<span class="social" style="left:776px"></span>
<span class="paycard" style="left:916px;background:#c9d2e8"></span>
<span class="paycard" style="left:966px;background:#b8d2e4"></span>
<span class="paycard" style="left:1016px;background:#f2c6a8"></span>

</body>
</html>
```